New Packaging Design Project

Wine packaging redesign. Retail partner requested a redesign of a private label wine. The old label is attached. Our partner liked the Lantern and Briar label and wanted something similar. There will be a logo added to the top of the label

Went on vacation/holiday

```html
<!DOCTYPE html>
<html lang="en">
<head>
<meta charset="utf-8">
<title>Napa Valley Red Blend – Label Designs</title>
<link rel="stylesheet" href="https://fonts.googleapis.com/css2?family=Poiret+One&family=Cinzel:wght@400;500&display=swap">
<style>
  :root {
    --backdrop: #f4f4f4;
    --label-black: #1c1c1e;
    --label-edge: #262628;
    --gold: #d4b05a;
    --gold-deep: #a9852f;
    --ink-light: #e9e6df;
    --ink-muted: #c9c6bf;
    --etch-light: #f2f2f2;
    --etch-mid: #b9b9b9;
  }
  * { box-sizing: border-box; margin: 0; padding: 0; }
  html, body {
    width: 1200px; height: 935px; overflow: hidden;
    background: var(--backdrop);
  }
  .canvas { position: relative; width: 1200px; height: 935px; }

  .label {
    position: absolute;
    top: 403px;
    width: 270px;
    height: 445px;
    background: linear-gradient(180deg, var(--label-edge), var(--label-black) 40%, var(--label-edge));
    color: var(--ink-light);
    text-align: center;
  }
  .label--crest { left: 177px; }
  .label--wordmark { left: 753px; }

  .label__band {
    position: absolute; left: 0; right: 0; height: 4px;
    background: linear-gradient(90deg, var(--gold-deep), var(--gold) 50%, var(--gold-deep));
  }
  .label__band--top { top: 0; }
  .label__band--bottom { bottom: 0; }

  .brand {
    position: absolute; left: 0; right: 0;
    display: flex; align-items: center; justify-content: center; gap: 6px;
    font-family: "Cinzel", serif; font-size: 11px; letter-spacing: 2px;
    color: var(--gold);
  }
  .brand__dot {
    width: 8px; height: 8px; border: 1px solid var(--gold); border-radius: 50%;
  }

  .region {
    position: absolute; left: 0; right: 0;
    font-family: "Poiret One", sans-serif;
    color: var(--gold);
    line-height: 1;
  }
  .variety {
    position: absolute; left: 0; right: 0;
    font-family: "Cinzel", serif; font-weight: 500;
    line-height: 1;
  }
  .grapes {
    position: absolute; left: 0; right: 0;
    font-family: "Cinzel", serif;
    color: var(--ink-muted);
    line-height: 1.55;
    letter-spacing: 0.3px;
  }
  .vintage {
    position: absolute; left: 0; right: 0;
    font-family: "Poiret One", sans-serif;
    line-height: 1;
  }
  .vista {
    position: absolute; left: 0; right: 0;
    background: linear-gradient(180deg, var(--etch-light) 0%, #dedede 35%, var(--etch-mid) 70%, #8f8f8f 100%);
  }

  /* crest layout */
  .label--crest .brand { top: 46px; }
  .label--crest .region { top: 98px; font-size: 28px; letter-spacing: 3px; }
  .label--crest .variety { top: 132px; font-size: 10px; letter-spacing: 3px; }
  .label--crest .vista { top: 160px; height: 150px; }
  .label--crest .grapes { top: 333px; font-size: 8px; }
  .label--crest .vintage { top: 382px; font-size: 19px; letter-spacing: 1px; }

  /* wordmark layout */
  .label--wordmark .region { top: 55px; font-size: 41px; letter-spacing: 4px; }
  .label--wordmark .variety { top: 140px; font-size: 15px; letter-spacing: 4px; }
  .label--wordmark .grapes { top: 198px; font-size: 9px; }
  .label--wordmark .vintage { top: 244px; font-size: 21px; letter-spacing: 1px; }
  .label--wordmark .vista { top: 288px; height: 150px; }
</style>
</head>
<body>
<main class="canvas">

  <section class="label label--crest">
    <div class="label__band label__band--top"></div>
    <div class="brand"><span class="brand__dot"></span>Northvale</div>
    <h1 class="region">NAPA VALLEY</h1>
    <p class="variety">RED BLEND</p>
    <div class="vista" role="img" aria-label="Engraved illustration of vineyard rows, a lone tree and rolling hills, with torn paper edges"></div>
    <p class="grapes">MERLOT | CABERNET SAUVIGNON<br>CABERNET FRANC | PETIT VERDOT | MALBEC</p>
    <p class="vintage">2018</p>
    <div class="label__band label__band--bottom"></div>
  </section>

  <section class="label label--wordmark">
    <div class="label__band label__band--top"></div>
    <h1 class="region">NAPA VALLEY</h1>
    <p class="variety">RED BLEND</p>
    <p class="grapes">MERLOT | CABERNET SAUVIGNON<br>CABERNET FRANC | PETIT VERDOT | MALBEC</p>
    <p class="vintage">2018</p>
    <div class="vista" role="img" aria-label="Engraved illustration of vineyard rows, a lone tree and rolling hills, with a torn paper top edge"></div>
    <div class="label__band label__band--bottom"></div>
  </section>

</main>
</body>
</html>
```